Business cards for education company

We need a business card design for a relatively new company based in Queensland and operating across Australia. We resell diploma level education courses which include Business, Management, Finance, Community Services & Government courses. We offer over 20 different courses.
The target market is for anyone 16 years of age and older. There is no age limit.

We would like to see the design use the color blue and silver. The final design should communicate professionalism and a bright future.

We sell education but are also promoting the career they see themselves in 2-3 years in the future

Our company logo is attached.

Target Market(s)

We target all age groups above 16 years of age. The main target market would be people aged between 17-35.

We focus on those people who cannot make it into University or do not want to commit the time to a full degree.

Industry/Entity Type

Education

Requirements
Must have
• Professional
Company logo
website
Contact details:

Please use the following example:

Lionel Parfitt
Senior Education Consultant
0417 386 591
Lionel.parfitt@brightwaylearninghub.com.au
www.brightwaylearninghub.com.au

```html
<!DOCTYPE html>
<html lang="en">
<head>
<meta charset="utf-8">
<title>Brightway Learning Hub – Business Card</title>
<link href="https://fonts.googleapis.com/css2?family=Open+Sans:wght@400;600&display=swap" rel="stylesheet">
<style>
  :root {
    --bg-top: #f4f4f4;
    --bg-bottom: #b9b9b9;
    --brand-blue: #0a5aa6;
    --text-blue: #0d55a0;
    --silver: #d9d9d9;
    --card-light: #f7f7f7;
    --card-mid: #e4e4e4;
    --pill: #d3d3d3;
    --edge: #3a3a3a;
  }
  * { margin: 0; padding: 0; box-sizing: border-box; }
  html, body { width: 1200px; height: 800px; overflow: hidden; }
  body {
    position: relative;
    background: linear-gradient(180deg, var(--bg-top) 0%, #e2e2e2 50%, var(--bg-bottom) 100%);
    font-family: "Open Sans", Arial, sans-serif;
  }
  .brand-mark {
    position: absolute;
    display: flex;
    align-items: center;
    gap: 22px;
  }
  .brand-mark .dot {
    border-radius: 50%;
    background: var(--brand-blue);
    flex: none;
  }
  .brand-mark .name {
    color: var(--brand-blue);
    font-weight: 600;
    white-space: nowrap;
  }
  .brand-mark--sheet { left: 62px; top: 112px; }
  .brand-mark--sheet .dot { width: 74px; height: 74px; }
  .brand-mark--sheet .name { font-size: 44px; }

  .card {
    position: absolute;
    left: 377px; top: 270px;
    width: 754px; height: 432px;
    background:
      radial-gradient(ellipse 320px 220px at 1000px 250px, #ffffff 0%, rgba(255,255,255,0) 100%) no-repeat,
      linear-gradient(180deg, var(--card-mid) 0%, var(--card-light) 55%, var(--card-mid) 100%);
    background-position: -377px -270px, 0 0;
    border-left: 2px solid var(--edge);
    box-shadow: 4px 5px 8px rgba(0,0,0,0.45);
    overflow: hidden;
  }
  .card__bands {
    position: absolute;
    left: 0; width: 100%; height: 32px;
    display: grid;
    grid-template-columns: 186px 187px 187px 1fr;
  }
  .card__bands--top { top: 0; }
  .card__bands--bottom { bottom: 2px; }
  .band--blue { background: var(--brand-blue); }
  .band--silver { background: var(--silver); }

  .brand-mark--card { left: 28px; top: 78px; gap: 14px; }
  .brand-mark--card .dot { width: 46px; height: 46px; }
  .brand-mark--card .name { font-size: 27px; }

  .card__holder {
    position: absolute;
    left: 0; top: 188px;
    width: 393px; height: 60px;
    background: var(--pill);
    border-radius: 0 14px 14px 0;
    padding: 0 0 0 28px;
    color: var(--text-blue);
  }
  .card__name { font-size: 28px; font-weight: 600; line-height: 32px; margin-top: -2px; }
  .card__role { font-size: 24px; font-weight: 400; line-height: 28px; }

  .card__phone {
    position: absolute;
    left: 465px; top: 194px;
    font-size: 31px;
    color: var(--text-blue);
    letter-spacing: 0.5px;
  }
  .card__links {
    position: absolute;
    right: 14px; top: 322px;
    text-align: right;
    color: var(--text-blue);
    font-size: 25px;
    line-height: 31px;
  }
</style>
</head>
<body>
  <div class="brand-mark brand-mark--sheet">
    <span class="dot"></span>
    <span class="name">Brightway Learning Hub</span>
  </div>

  <section class="card">
    <div class="card__bands card__bands--top">
      <span class="band--blue"></span><span class="band--silver"></span>
      <span class="band--blue"></span><span class="band--silver"></span>
    </div>

    <div class="brand-mark brand-mark--card">
      <span class="dot"></span>
      <span class="name">Brightway Learning Hub</span>
    </div>

    <div class="card__holder">
      <p class="card__name">Lionel Parfitt</p>
      <p class="card__role">Senior Education Consultant</p>
    </div>

    <p class="card__phone">0417 386 591</p>

    <div class="card__links">
      <p>www.brightwaylearninghub.com.au</p>
      <p>Lionel.parfitt@brightwaylearninghub.com.au</p>
    </div>

    <div class="card__bands card__bands--bottom">
      <span class="band--silver"></span><span class="band--blue"></span>
      <span class="band--silver"></span><span class="band--blue"></span>
    </div>
  </section>
</body>
</html>
```